Buchcover-Design für Fragenbuch
Ganz herzlichen Dank. Die Zusammenarbeit war völlig reibungslos und entspannt. Änderungswünsche wurden professionell umgesetzt und die kreativen Vorschläge fand ich super. Ich bin total glücklich mit dem Ergebnis.
Zielgruppe
Autorin und Workshopleiterin. Zielgruppe: Frauen ab 30
Aufgabenstellung
Ich benötige ein komplettes Buchcover, sowie 12 farbige Innenseiten. Es geht um ein Fragenbuch zum Ausfüllen mit dem Titel:
„Finde zurück zur leisen Mitte
Ein Arbeitsheft zum Eintragen für tiefere seelische Ruhe“
Das Format des Buches beträgt 17x22cm. Es ist in 12 Wochen unterteilt. Darum hätte ich gerne zwischen den einzelnen Wochen eine farbige Seite (1. Woche, 2. Woche etc.), die designmäßig mit dem Außencover korrespondiert.
Die Farben sollten eher zart oder gedeckt sein. Auf keinen Fall jedoch kitschig. Wichtig ist mir, dass keine bestimmte Person zu sehen ist. (Foto)
Das ist meine Website www.finde-zurueck-zur-leisen-mitte.de

```html
<!DOCTYPE html>
<html lang="de">
<head>
<meta charset="utf-8">
<title>Finde zurück zur leisen Mitte – Cover und Innenseiten</title>
<link rel="stylesheet" href="https://fonts.googleapis.com/css2?family=Josefin+Sans:wght@200;300;400&family=Great+Vibes&family=Cormorant+Garamond:wght@400&family=Open+Sans:wght@400;700&display=swap">
<style>
  :root{
    --stage:#c9c9c9;
    --week-red:#8e2f33;
    --week-red-deep:#6a2529;
    --cover-rose:#ad5f5f;
    --peach:#f1d2c3;
    --line-light:#f3d9cf;
    --ink-dark:#2b1416;
    --paper:#f7f6f4;
    --sepia-light:#c8b2a2;
    --sepia-dark:#5b4234;
  }
  *{margin:0;padding:0;box-sizing:border-box}
  html,body{width:1200px;height:960px;overflow:hidden}
  body{background:var(--stage);position:relative;font-family:"Josefin Sans",sans-serif}

  .page{position:absolute;top:250px;width:356px;height:460px;overflow:hidden}

  /* Week divider page */
  .week-page{left:42px;background:var(--week-red)}
  .week-page .frame{position:absolute;inset:0}
  .week-number{position:absolute;left:34px;top:26px;font-weight:200;font-size:180px;line-height:1;color:var(--peach)}
  .week-label{position:absolute;left:120px;top:118px;font-weight:200;font-size:50px;line-height:1;color:var(--peach);white-space:nowrap}
  .week-title{position:absolute;left:122px;top:178px;font-weight:300;font-size:28px;line-height:1;color:var(--ink-dark);white-space:nowrap}
  .week-rule{position:absolute;left:122px;top:218px;width:180px;height:1px;background:var(--line-light)}
  .week-number-ghost{position:absolute;right:34px;top:280px;font-weight:200;font-size:150px;line-height:1;color:var(--peach);opacity:.28}
  .arch-outer{position:absolute;left:40px;bottom:0;width:196px;height:190px;background:var(--week-red-deep);border-radius:98px 98px 0 0}
  .arch-photo{position:absolute;left:66px;bottom:0;width:144px;height:164px;border-radius:72px 72px 0 0;background:linear-gradient(160deg,#f2f2f0,#d8d6d2)}

  /* Photo page */
  .photo-page{left:398px;background:var(--paper)}
  .photo-top{position:absolute;left:28px;top:30px;width:300px;height:178px;background:linear-gradient(135deg,var(--sepia-light),#8e7363 55%,var(--sepia-dark))}
  .photo-side{position:absolute;left:160px;top:222px;width:196px;height:180px;background:linear-gradient(160deg,#6d5446,#3a2a22 70%)}
  .body-copy{position:absolute;left:28px;top:226px;width:118px;font-family:"Open Sans",sans-serif;font-size:6.4px;line-height:1.55;color:#3a3a3a}
  .wave-divider{position:absolute;left:28px;top:330px}
  .caption{position:absolute;left:28px;top:344px;width:118px;font-family:"Open Sans",sans-serif;font-weight:700;font-size:6.4px;line-height:1.5;color:var(--ink-dark)}
  .zigzag{position:absolute;left:28px;top:420px}

  /* Cover */
  .cover{left:802px;background:linear-gradient(180deg,#a85656,var(--cover-rose) 60%,#b26868)}
  .cover .frame{position:absolute;inset:0}
  .cover-title{position:absolute;left:0;right:0;top:66px;text-align:center;font-weight:300;font-size:34px;line-height:1.04;letter-spacing:.5px;color:var(--line-light);text-transform:uppercase}
  .cover-kicker{position:absolute;left:0;right:0;top:232px;text-align:center;font-weight:300;font-size:18px;letter-spacing:.5px;color:var(--ink-dark);text-transform:uppercase}
  .cover-subline{position:absolute;left:0;right:0;top:258px;text-align:center;font-weight:300;font-size:8.2px;line-height:1.3;color:var(--ink-dark);text-transform:uppercase}
  .cover-author{position:absolute;left:0;right:0;top:330px;text-align:center;font-family:"Great Vibes",cursive;font-size:26px;color:var(--line-light)}
  .cover-services{position:absolute;left:0;right:0;top:374px;text-align:center;font-family:"Cormorant Garamond",serif;font-size:8px;line-height:1.5;letter-spacing:.5px;color:var(--line-light)}
  .cover-services .dot{display:block;width:3px;height:3px;margin:2px auto;border-radius:50%;background:var(--line-light)}
</style>
</head>
<body>

  <section class="page week-page" aria-label="Innenseite Woche 3">
    <svg class="frame" width="356" height="460" aria-hidden="true">
      <line x1="22" y1="0" x2="22" y2="460" stroke="#e8b9ad" stroke-width=".7" opacity=".7"/>
      <line x1="338" y1="0" x2="338" y2="460" stroke="#e8b9ad" stroke-width=".7" opacity=".7"/>
      <line x1="0" y1="20" x2="356" y2="20" stroke="#e8b9ad" stroke-width=".7" opacity=".7"/>
      <line x1="0" y1="440" x2="356" y2="440" stroke="#e8b9ad" stroke-width=".7" opacity=".7"/>
    </svg>
    <div class="week-number">3</div>
    <div class="week-label">WOCHE</div>
    <div class="week-title">TITLE HERE</div>
    <div class="week-rule"></div>
    <div class="week-number-ghost">3</div>
    <div class="arch-outer"></div>
    <div class="arch-photo" role="img" aria-label="Foto: Oberkörper in hellem Strickpullover mit Kettenanhänger, ohne Gesicht"></div>
  </section>

  <section class="page photo-page" aria-label="Innenseite mit Bildern">
    <div class="photo-top" role="img" aria-label="Foto in Sepia: Rosen und Monstera-Blätter"></div>
    <p class="body-copy">Aliquam at lectus id arcu porta sodales quis posuere justo. In mi nisl, cursus in lacus nec, maximus tempus elit. In hac habitasse platea dictumst. Vivamus sed dignissim dui. Vivamus rutrum, risus dapibus suscipit pulvinar, ex quam congue nunc, quis imperdiet nunc nulla non mauris.</p>
    <svg class="wave-divider" width="40" height="6" aria-hidden="true">
      <polyline points="0,3 4,1 8,5 12,1 16,5 20,1 24,5 28,1 32,5 36,1 40,3" fill="none" stroke="#6a6a6a" stroke-width=".6"/>
    </svg>
    <p class="caption">Aliquam at lectus id arcu porta sodales quis posuere</p>
    <div class="photo-side" role="img" aria-label="Foto in Sepia: Wand mit Lampen und Leuchtschrift"></div>
    <svg class="zigzag" width="300" height="8" aria-hidden="true">
      <polyline points="0,4 4,1 8,7 12,1 16,7 20,1 24,7 28,1 32,7 36,1 40,7 44,1 48,7 52,1 56,7 60,1 64,7 68,1 72,7 76,1 80,7 84,1 88,7 92,1 96,7 100,1 104,7 108,1 112,7 116,1 120,7 124,1 128,7 132,1 136,7 140,1 144,7 148,1 152,7 156,1 160,7 164,1 168,7 172,1 176,7 180,1 184,7 188,1 192,7 196,1 200,7 204,1 208,7 212,1 216,7 220,1 224,7 228,1 232,7 236,1 240,7 244,1 248,7 252,1 256,7 260,1 264,7 268,1 272,7 276,1 280,7 284,1 288,7 292,1 296,7 300,4" fill="none" stroke="#8a8a8a" stroke-width=".6"/>
    </svg>
  </section>

  <section class="page cover" aria-label="Buchcover">
    <svg class="frame" width="356" height="460" aria-hidden="true">
      <line x1="22" y1="0" x2="22" y2="460" stroke="#f3d9cf" stroke-width=".8"/>
      <line x1="334" y1="0" x2="334" y2="460" stroke="#f3d9cf" stroke-width=".8"/>
      <line x1="0" y1="24" x2="356" y2="24" stroke="#f3d9cf" stroke-width=".8"/>
      <line x1="0" y1="436" x2="356" y2="436" stroke="#f3d9cf" stroke-width=".8"/>
      <path d="M48 436 V 450 M48 436 A130 130 0 0 1 308 436 V 450" fill="none" stroke="#f3d9cf" stroke-width=".8" transform="translate(0,-6)"/>
    </svg>
    <h1 class="cover-title">Finde<br>zurück<br>zur leisen<br>Mitte</h1>
    <p class="cover-kicker">Ein Arbeitsheft</p>
    <p class="cover-subline">zum Eintragen<br>für tiefere seelische Ruhe</p>
    <p class="cover-author">by Lena Hartwig</p>
    <p class="cover-services">COACHING<span class="dot"></span>MENTORING<span class="dot"></span>2021</p>
  </section>

</body>
</html>
```